Create website design - Hire business

Build website to specification. Look and feel only or include all functionality. I have put together a google document which includes all information on requirements. I will share this with you via message once you have been assigned the job.

Coding

Coded - Design and coding required

Number of Pages Required

1 page

Requirements
Must have
• As per Google Doc
Nice to have
• As per Google Doc
Should not have
• As per Google Doc

```html
<!DOCTYPE html>
<html lang="en">
<head>
<meta charset="utf-8">
<title>Kerbside Hire</title>
<link rel="stylesheet" href="https://fonts.googleapis.com/css2?family=Bitter:wght@600;700&family=Inter:wght@400;500&display=swap">
<style>
:root{
  --blue:#2b7cc7;
  --blue-soft:#a9cbe8;
  --ink:#222a33;
  --muted:#9aa6b2;
  --field:#dde8ea;
  --card:#eaf2fa;
  --card-active:#d4e4f4;
  --white:#ffffff;
}
*{box-sizing:border-box;margin:0;padding:0}
html,body{width:1200px;height:4307px;overflow:hidden}
body{position:relative;background:var(--white);font-family:"Inter",sans-serif;color:var(--ink)}
.abs{position:absolute}
.serif{font-family:"Bitter",serif;font-weight:700;color:var(--blue);text-transform:uppercase}
.btn{position:absolute;display:flex;align-items:center;justify-content:center;background:var(--blue);color:var(--white);border-radius:27px;font-family:"Bitter",serif;font-weight:700;font-size:20px;text-transform:uppercase}
.section-title{position:absolute;left:0;width:1200px;text-align:center;font-size:33px}
.lines{white-space:nowrap}

/* header */
.logo{left:112px;top:28px;font-size:30px}
.nav{left:438px;top:37px;font-size:17px;font-weight:500}
.nav span{position:absolute;white-space:nowrap}
.search-icon{left:1045px;top:25px;width:46px;height:46px;border-radius:50%;background:var(--blue);box-shadow:0 0 0 3px #cfe1f2}

/* hero */
.hero{left:0;top:90px;width:1200px;height:598px;background:linear-gradient(100deg,#6f6a66 0%,#b9b3ab 35%,#e8e6e2 60%,#f6f6f5 100%)}
.hero-text{right:112px;top:196px;width:640px;text-align:right}
.hero-text .welcome{font-size:21px}
.hero-text h1{font-size:38px;margin-top:8px}
.hero-text p{font-size:19px;line-height:38px;margin-top:12px;color:#333}
.search-box{left:80px;top:628px;width:1038px;height:184px;background:var(--white);border-radius:33px;box-shadow:0 4px 14px rgba(0,0,0,.12)}
.field-label{top:28px;font-size:19px}
.field{top:74px;width:222px;height:47px;background:var(--field);font-size:16px;padding:0 16px;display:flex;align-items:center;color:#333}

/* about */
.about-text{left:61px;top:1055px;width:500px;text-align:right;font-size:19.5px;line-height:40.2px;color:#333}
.about-shape{left:765px;top:1003px;width:435px;height:598px;background:var(--blue-soft);border-radius:110px 0 0 110px}
.about-photo{left:600px;top:1053px;width:541px;height:498px;background:linear-gradient(135deg,#d9d2c7,#8e8a86 55%,#2c3d52)}

/* categories */
.cat-img{width:127px;height:132px;border-radius:8px;border:3px solid var(--blue-soft)}
.cat-title{font-size:25px}
.cat-text{font-size:19.5px;line-height:40px;color:#333}

/* testimonials */
.t-card{top:2336px;height:441px;background:var(--card);border-radius:14px;text-align:center}
.t-card.active{background:var(--card-active)}
.t-card.faded{opacity:.55}
.avatar{position:absolute;left:50%;top:29px;margin-left:-58px;width:116px;height:116px;border-radius:50%;border:3px solid #9aa6b2;background:linear-gradient(160deg,#cfd3d6,#7c8792)}
.t-name{position:absolute;left:0;width:100%;top:170px;font-size:20px}
.t-text{position:absolute;left:0;width:100%;top:212px;font-size:19.5px;line-height:40px;color:#4a5560}
.t-icons{position:absolute;left:50%;top:366px;margin-left:-54px;display:flex;gap:20px}
.ic{width:44px;height:44px;border-radius:50%;background:var(--blue);display:flex;align-items:center;justify-content:center}
.ic-ring{width:14px;height:14px;border-radius:50%;border:2.5px solid var(--white)}
.dot{top:2822px;width:14px;height:14px;border-radius:50%;background:var(--blue-soft)}

/* newsletter */
.newsletter{left:112px;top:2926px;width:976px;height:391px;border-radius:33px;background:linear-gradient(180deg,#1f2429 0%,#3a4047 55%,#272c33 100%);text-align:center;color:var(--white)}
.newsletter h2{font-family:"Bitter",serif;font-weight:700;font-size:33px;margin-top:46px}
.newsletter h3{font-family:"Bitter",serif;font-weight:700;font-size:21px;margin-top:22px}
.newsletter p{font-size:19.5px;line-height:40px;margin-top:16px}
.sub-input{left:219px;top:281px;width:538px;height:53px;background:var(--white);border-radius:27px;text-align:left;padding-left:25px;font-size:20px;color:#333;display:flex;align-items:center}

/* blogs */
.blog-img{top:3504px;width:314px;height:254px}
.blog-date{top:3497px;width:40px;height:48px;background:var(--blue);color:var(--white);font-family:"Bitter",serif;font-weight:700;font-size:10px;text-align:center;padding-top:8px;line-height:15px}
.blog-text{top:3784px;font-size:18.5px;line-height:34px;color:#222;white-space:nowrap}
.read-more{top:3900px;font-size:17px;text-decoration:underline}

/* footer */
.footer{left:0;top:4010px;width:1200px;height:297px;background:var(--blue);color:var(--white);text-align:center}
.footer .f-name{font-family:"Bitter",serif;font-weight:700;font-size:32px;margin-top:44px}
.f-nav span{position:absolute;top:114px;font-size:17px;font-weight:500}
.f-social{position:absolute;top:174px;width:42px;height:42px;border-radius:50%;background:var(--white);display:flex;align-items:center;justify-content:center}
.f-social .ic-ring{border-color:var(--blue)}
.copyright{position:absolute;left:0;width:100%;top:236px;font-size:13px;font-weight:500}
</style>
</head>
<body>

<!-- header -->
<div class="abs serif logo">Kerbside Hire</div>
<div class="abs nav">
  <span style="left:0">ABOUT</span>
  <span style="left:103px">CONTACT</span>
  <span style="left:230px">TERMS</span>
  <span style="left:332px">PRIVACY</span>
  <span style="left:448px">SERVICES</span>
</div>
<div class="abs search-icon">
  <svg width="46" height="46" viewBox="0 0 46 46"><circle cx="21" cy="21" r="8" fill="none" stroke="#fff" stroke-width="2.5"/><line x1="27" y1="27" x2="32" y2="32" stroke="#fff" stroke-width="2.5" stroke-linecap="round"/></svg>
</div>

<!-- hero -->
<div class="abs hero" role="img" aria-label="Worker in a hard hat climbing a ladder"></div>
<div class="abs hero-text">
  <div class="serif welcome">Welcome to</div>
  <h1 class="serif">Kerbside Hire</h1>
  <p class="lines">Nemo enim ipsam voluptatem quia voluptas sit<br>aspernatur aut odit aut fugit, sed quia<br>consequuntur magni dolores eos qui ratione</p>
</div>
<div class="btn" style="left:891px;top:443px;width:197px;height:52px">Get Started</div>

<div class="abs search-box">
  <div class="abs serif field-label" style="left:34px">Location</div>
  <div class="abs serif field-label" style="left:283px">Product</div>
  <div class="abs serif field-label" style="left:530px">From</div>
  <div class="abs serif field-label" style="left:781px">To</div>
  <div class="abs field" style="left:34px">Enter Your Location</div>
  <div class="abs field" style="left:283px">Select</div>
  <div class="abs field" style="left:530px">DD/MM/YYYY</div>
  <div class="abs field" style="left:781px">DD/MM/YYYY</div>
</div>
<div class="btn" style="left:501px;top:780px;width:197px;height:54px">Search Now</div>

<!-- about -->
<h2 class="serif section-title" style="top:912px">About Us</h2>
<p class="abs about-text lines">Lorem ipsum dolor sit amet, consectetur<br>adipiscing elit, sed do eiusmod tempor<br>incididunt ut labore et dolore magna aliqua. Ut<br>enim ad minim veniam, quis nostrud exercitation<br>ullamco laboris nisi ut aliquip ex ea commodo<br>consequat. Duis aute irure dolor in reprehenderit<br>in voluptate velit esse cillum dolore eu fugiat<br>nulla pariatur. Excepteur sint occaecat cupidatat<br>non proident, sunt in culpa qui officia deserunt</p>
<div class="btn" style="left:364px;top:1454px;width:197px;height:53px">Learn Now</div>
<div class="abs about-shape"></div>
<div class="abs about-photo" role="img" aria-label="Smiling businesswoman seated at a desk"></div>

<!-- categories -->
<h2 class="serif section-title" style="top:1679px">Catagories</h2>
<div class="abs cat-img" style="left:134px;top:1766px;background:linear-gradient(180deg,#dfe7ee,#7fa3c2)" role="img" aria-label="Ladder rising into clouds"></div>
<div class="abs serif cat-title" style="left:287px;top:1766px">Ladder</div>
<div class="abs cat-text lines" style="left:287px;top:1815px">Sed ut perspiciatis unde omnis<br>iste natus error sit voluptatem</div>

<div class="abs cat-img" style="left:622px;top:1766px;background:linear-gradient(180deg,#8f8c8a,#4f4a47)" role="img" aria-label="Hammer on a grey surface"></div>
<div class="abs serif cat-title" style="left:775px;top:1766px">Hammer</div>
<div class="abs cat-text lines" style="left:775px;top:1815px">Sed ut perspiciatis unde omnis<br>iste natus error sit voluptatem</div>

<div class="abs cat-img" style="left:134px;top:1927px;background:linear-gradient(135deg,#3a3a3a,#8a2a26 60%,#222)" role="img" aria-label="Hands using a power drill"></div>
<div class="abs serif cat-title" style="left:287px;top:1927px">Drill</div>
<div class="abs cat-text lines" style="left:287px;top:1976px">Sed ut perspiciatis unde omnis<br>iste natus error sit voluptatem</div>

<div class="abs cat-img" style="left:622px;top:1927px;background:linear-gradient(135deg,#b8a48a,#d9cbb6 50%,#5b6f8a)" role="img" aria-label="Mover pushing boxes on a trolley"></div>
<div class="abs serif cat-title" style="left:775px;top:1927px">Moving Trolley</div>
<div class="abs cat-text lines" style="left:775px;top:1976px">Sed ut perspiciatis unde omnis<br>iste natus error sit voluptatem</div>

<div class="btn" style="left:501px;top:2109px;width:197px;height:53px">View More</div>

<!-- testimonials -->
<h2 class="serif section-title" style="top:2244px">Testimonials</h2>

<div class="abs t-card faded" style="left:0;width:389px">
  <div class="avatar" role="img" aria-label="Customer portrait"></div>
  <div class="serif t-name">Lorem Ipsum</div>
  <div class="t-text">Sed ut perspiciatis unde omnis<br>iste natus error sit voluptatem<br>accusantium doloremque</div>
  <div class="t-icons"><div class="ic"><div class="ic-ring"></div></div><div class="ic"><svg width="20" height="24" viewBox="0 0 20 24"><path d="M10 1a8 8 0 0 0-8 8c0 6 8 14 8 14s8-8 8-14a8 8 0 0 0-8-8z" fill="#fff"/><circle cx="10" cy="9" r="3" fill="#2b7cc7"/></svg></div></div>
</div>
<div class="abs t-card active" style="left:401px;width:398px">
  <div class="avatar" role="img" aria-label="Customer portrait"></div>
  <div class="serif t-name">Lorem Ipsum</div>
  <div class="t-text" style="color:#333">Sed ut perspiciatis unde omnis<br>iste natus error sit voluptatem<br>accusantium doloremque</div>
  <div class="t-icons"><div class="ic"><div class="ic-ring"></div></div><div class="ic"><svg width="20" height="24" viewBox="0 0 20 24"><path d="M10 1a8 8 0 0 0-8 8c0 6 8 14 8 14s8-8 8-14a8 8 0 0 0-8-8z" fill="#fff"/><circle cx="10" cy="9" r="3" fill="#2b7cc7"/></svg></div></div>
</div>
<div class="abs t-card faded" style="left:812px;width:388px">
  <div class="avatar" role="img" aria-label="Customer portrait"></div>
  <div class="serif t-name">Lorem Ipsum</div>
  <div class="t-text">Sed ut perspiciatis unde omnis<br>iste natus error sit voluptatem<br>accusantium doloremque</div>
  <div class="t-icons"><div class="ic"><div class="ic-ring"></div></div><div class="ic"><svg width="20" height="24" viewBox="0 0 20 24"><path d="M10 1a8 8 0 0 0-8 8c0 6 8 14 8 14s8-8 8-14a8 8 0 0 0-8-8z" fill="#fff"/><circle cx="10" cy="9" r="3" fill="#2b7cc7"/></svg></div></div>
</div>
<div class="abs dot" style="left:567px;background:var(--blue)"></div>
<div class="abs dot" style="left:593px"></div>
<div class="abs dot" style="left:619px"></div>

<!-- newsletter -->
<div class="abs newsletter" role="img" aria-label="Dim warehouse interior behind the subscription panel">
  <h2>NEWSLETTER SUBSCRIBE</h2>
  <h3>REDUCES WASTE AND HELPS THE ENVIRONMENT</h3>
  <p>Sed ut perspiciatis unde omnis iste natus error sit voluptatem<br>accusantium doloremque laudantium, totam rem aperiam.</p>
  <div class="abs sub-input">Best time to get jobs</div>
  <div class="btn" style="left:581px;top:284px;width:173px;height:47px">Discount</div>
</div>

<!-- blogs -->
<h2 class="serif section-title" style="top:3400px">Latest Blogs</h2>
<div class="abs blog-img" style="left:112px;background:linear-gradient(135deg,#4f7a3c,#c99a5a 55%,#e6dcc8)" role="img" aria-label="Camping tent and table outdoors"></div>
<div class="abs blog-img" style="left:441px;background:linear-gradient(135deg,#1e2a38,#4a6280 50%,#1a1f26)" role="img" aria-label="Mechanic working on an engine"></div>
<div class="abs blog-img" style="left:770px;background:linear-gradient(135deg,#6a5a48,#c9b08a 45%,#3d4a5a)" role="img" aria-label="Worker carrying boxes in a warehouse aisle"></div>
<div class="abs blog-date" style="left:130px">21<br>AUG</div>
<div class="abs blog-date" style="left:459px">17<br>AUG</div>
<div class="abs blog-date" style="left:788px">16<br>AUG</div>
<p class="abs blog-text" style="left:112px">Lorem ipsum dolor sit amet,<br>consectetur adipiscing elit, sed do<br>eiusmod tempor incididunt ut</p>
<p class="abs blog-text" style="left:441px">Lorem ipsum dolor sit amet,<br>consectetur adipiscing elit, sed<br>do eiusmod tempor incididunt ut</p>
<p class="abs blog-text" style="left:770px">Lorem ipsum dolor sit amet,<br>consectetur adipiscing elit, sed<br>do eiusmod tempor incididunt ut</p>
<div class="abs serif read-more" style="left:112px">Read More</div>
<div class="abs serif read-more" style="left:441px">Read More</div>
<div class="abs serif read-more" style="left:770px">Read More</div>

<!-- footer -->
<div class="abs footer">
  <div class="f-name">KERBSIDE HIRE</div>
  <div class="f-nav">
    <span style="left:334px">ABOUT</span>
    <span style="left:440px">CONTACT</span>
    <span style="left:566px">TERMS</span>
    <span style="left:668px">PRIVACY</span>
    <span style="left:783px">SERVICES</span>
  </div>
  <div class="f-social" style="left:488px"><div class="ic-ring"></div></div>
  <div class="f-social" style="left:548px"><div class="ic-ring"></div></div>
  <div class="f-social" style="left:608px"><div class="ic-ring"></div></div>
  <div class="f-social" style="left:668px"><div class="ic-ring"></div></div>
  <div class="copyright">@2023 COPYRIGHTS. KERBSIDE HIRE. <u>AUSTRALIAN PRIVACY ACT</u>. ALL RIGHTS RESERVED.</div>
</div>

</body>
</html>
```